Inspirational Quote Poster for Employees

For this project, we need a simple yet high-impact poster template that will be customized for each of our employees with a personalized inspirational quote and color scheme. This template should allow us to quickly and easily customize the text and colors in the poster without a lot of effort.

The poster design should consist of:
- A stylized text area to contain the main text of the quote
- A separate text area to contain the source of quote
- A background that complements the color and style of the text

Text may use different typographic effects (such as color, stroke weight, italicization, font size changes, drop shadows) to draw attention to words in the quote; the source of the quote may be formatted the same as the main text of the quote, or may be formatted differently to distinguish it from the main quote.

The background may be simply a single color, subtle texture, gradients, halftone effects, or other color/texture effects may be used to complement the text.

Examples of the types of posters envisioned by this project:
- http://www.pinvelora.example/marcusdtelford/quillbase-job-1/

Sample quotes to use to build your poster - choose whichever one you want, but be certain that the poster design will handle both long and short quotes:
- "Happiness in intelligent people is the rarest thing I know" - Walden Prosket
- "Wanting to be someone else is a waste of the person you are." - Rolf Dintey
- "Experience is not what happens to you. It is what you do with what happens to you." - Ferris Mundell
- "Simplicity is the ultimate in sophistication." - Rinaldo de Pavesco
- "You will get all you want in life if you help enough other people get what they want." - Tad Pomfrey
- "Hell, there are no rules here — we're trying to accomplish something." - Gareth Vullane

Industry/Entity Type

Quote

Requirements
Must have
• Final deliverable must be:
• - Formatted for an 18” x 24” poster (in portrait orientation)
• - Delivered in Adobe InDesign, Adobe Illustrator, or Extended PostScript format
• - Use CMYK color mode
• - Be print-ready at 300dpi resolution
• - Include any fonts used in the template

```html
<!DOCTYPE html>
<html lang="en">
<head>
<meta charset="utf-8">
<title>Quote Poster – Ferris Mundell</title>
<link rel="stylesheet" href="https://fonts.googleapis.com/css2?family=Quicksand:wght@400&family=Montserrat:wght@700&display=swap">
<style>
  :root {
    --ink: #ffffff;
    --bg-top: #7e7e7e;
    --bg-mid: #6a5a66;
    --bg-low: #3a2f2a;
    --bg-bottom: #161616;
    --glow-blue: rgba(70, 92, 200, 0.95);
    --glow-violet: rgba(178, 146, 232, 0.95);
    --glow-red: rgba(246, 88, 70, 0.95);
    --glow-orange: rgba(255, 140, 60, 0.95);
    --glow-peach: rgba(222, 150, 100, 0.95);
    --glow-rose: rgba(208, 122, 130, 0.9);
    --glow-sage: rgba(150, 172, 156, 0.8);
    --glow-amber: rgba(230, 160, 90, 0.75);
    --shadow: rgba(0, 0, 0, 0.3);
  }
  html, body {
    margin: 0;
    padding: 0;
    width: 848px;
    height: 1200px;
    overflow: hidden;
  }
  .poster {
    position: relative;
    width: 848px;
    height: 1200px;
    overflow: hidden;
    background:
      radial-gradient(ellipse 190px 170px at 350px 450px, var(--glow-violet), transparent 100%),
      radial-gradient(ellipse 210px 320px at 50px 470px, var(--glow-blue), transparent 100%),
      radial-gradient(ellipse 200px 170px at 520px 200px, var(--glow-sage), transparent 100%),
      radial-gradient(ellipse 280px 230px at 460px 720px, var(--glow-red), transparent 100%),
      radial-gradient(ellipse 260px 230px at 670px 780px, var(--glow-orange), transparent 100%),
      radial-gradient(ellipse 200px 280px at 830px 480px, var(--glow-peach), transparent 100%),
      radial-gradient(ellipse 200px 200px at 100px 730px, var(--glow-rose), transparent 100%),
      radial-gradient(ellipse 240px 150px at 300px 880px, var(--glow-amber), transparent 100%),
      radial-gradient(ellipse 300px 200px at 250px 580px, rgba(120, 80, 170, 0.6), transparent 100%),
      linear-gradient(180deg, var(--bg-top) 0%, #737680 25%, var(--bg-mid) 50%, #5a4036 72%, var(--bg-low) 82%, var(--bg-bottom) 94%);
  }
  .quote {
    position: absolute;
    left: 148px;
    top: 182px;
    margin: 0;
    color: var(--ink);
    text-transform: uppercase;
    text-shadow: 0 2px 4px var(--shadow);
  }
  .quote__line {
    display: block;
    white-space: nowrap;
  }
  .quote__lead .quote__line {
    font-family: "Quicksand", sans-serif;
    font-weight: 400;
    font-size: 78px;
    line-height: 87px;
  }
  .quote__mark {
    position: absolute;
    transform: translateX(-100%);
    margin-left: -2px;
  }
  .quote__emphasis .quote__line {
    font-family: "Montserrat", sans-serif;
    font-weight: 700;
    font-size: 74px;
    line-height: 85px;
    padding-left: 8px;
  }
  .quote__emphasis .quote__line:nth-child(2) {
    padding-left: 10px;
  }
  .quote__emphasis .quote__line:nth-child(3),
  .quote__emphasis .quote__line:nth-child(4),
  .quote__emphasis .quote__line:nth-child(5) {
    padding-left: 18px;
  }
  .source {
    position: absolute;
    left: 397px;
    top: 985px;
    margin: 0;
    color: var(--ink);
    font-family: "Quicksand", sans-serif;
    font-weight: 400;
    font-size: 27px;
    line-height: 27px;
    letter-spacing: 2px;
    text-transform: uppercase;
    white-space: nowrap;
    text-shadow: 0 1px 3px var(--shadow);
  }
</style>
</head>
<body>
  <main class="poster">
    <blockquote class="quote">
      <span class="quote__lead">
        <span class="quote__line"><span class="quote__mark">“</span>Experience</span>
        <span class="quote__line">is not what</span>
        <span class="quote__line">happens to</span>
        <span class="quote__line">you.</span>
      </span>
      <span class="quote__emphasis">
        <span class="quote__line">It is what</span>
        <span class="quote__line">you do with</span>
        <span class="quote__line">what</span>
        <span class="quote__line">happens to</span>
        <span class="quote__line">you”</span>
      </span>
    </blockquote>
    <p class="source">- Ferris Mundell</p>
  </main>
</body>
</html>
```